HarlowForge Cards for contracting company

Design a sleek business card for contracting business.
Dale Morrow
President
405.618.7734
dale@harlowforge.com
www.harlowforge.com
Lic #: 3917258
Residential/Commerical
We are a roofing and construction contractor who like the colors of black & gold

I have a QR code to add.

• Dale Morrow

```html
<!DOCTYPE html>
<html lang="en">
<head>
<meta charset="utf-8">
<title>HarlowForge Business Cards</title>
<link rel="stylesheet" href="https://fonts.googleapis.com/css2?family=Archivo:wght@800&family=Questrial&display=swap">
<style>
  :root {
    --backdrop: #a7a7a7;
    --card-black: #050607;
    --ink: #111111;
    --white: #f4f4f4;
    --gold-light: #f0c96f;
    --gold-mid: #c9a052;
    --gold-deep: #8a6526;
    --gold-sheen: linear-gradient(100deg, #f3cc72 0%, #d4aa5a 22%, #8e6a2b 45%, #d2a95a 68%, #f0c96f 100%);
  }
  * { box-sizing: border-box; margin: 0; padding: 0; }
  html, body {
    width: 1200px;
    height: 1200px;
    overflow: hidden;
    background: var(--backdrop);
    font-family: "Questrial", "Helvetica Neue", Arial, sans-serif;
  }
  .card {
    position: absolute;
    left: 172px;
    width: 857px;
    height: 500px;
    background: var(--card-black);
    overflow: hidden;
  }
  .card--front { top: 76px; }
  .card--back { top: 621px; }

  .gold-band {
    position: absolute;
    left: 0;
    right: 0;
    background: var(--gold-sheen);
    color: var(--ink);
    display: flex;
    align-items: center;
    justify-content: center;
    letter-spacing: 0.5px;
  }
  .card--front .gold-band {
    left: 400px;
    top: 225px;
    height: 44px;
    padding-left: 100px;
    font-size: 22px;
  }
  .card--back .gold-band {
    top: 336px;
    height: 53px;
    font-size: 27px;
  }

  .gold-arc {
    position: absolute;
    left: 0;
    top: 0;
    width: 857px;
    height: 500px;
  }

  .brand {
    position: absolute;
    display: flex;
    align-items: center;
    gap: 14px;
    color: var(--gold-light);
    white-space: nowrap;
  }
  .brand__dot {
    border-radius: 50%;
    background: var(--gold-light);
  }
  .card--front .brand {
    left: 560px;
    top: 120px;
    font-size: 40px;
  }
  .card--front .brand__dot { width: 28px; height: 28px; }
  .card--back .brand {
    left: 50%;
    top: 175px;
    transform: translateX(-50%);
    font-size: 50px;
  }
  .card--back .brand__dot { width: 34px; height: 34px; }

  .contact-block {
    position: absolute;
    left: 96px;
    top: 210px;
    color: var(--ink);
  }
  .contact-block__name {
    font-family: "Archivo", "Arial Black", sans-serif;
    font-weight: 800;
    font-size: 35px;
    line-height: 44px;
    letter-spacing: 0.5px;
  }
  .contact-block__title {
    font-size: 21px;
    margin-top: 8px;
    letter-spacing: 0.5px;
  }
  .contact-list {
    list-style: none;
    margin-top: 32px;
  }
  .contact-list li {
    display: flex;
    align-items: center;
    gap: 14px;
    font-size: 22px;
    height: 37.5px;
    letter-spacing: 0.5px;
  }
  .contact-list svg {
    width: 17px;
    height: 17px;
    fill: var(--ink);
    flex: none;
  }

  .license {
    position: absolute;
    left: 562px;
    top: 400px;
    color: var(--white);
    font-size: 23px;
    letter-spacing: 0.5px;
  }
</style>
</head>
<body>

<section class="card card--front" aria-label="Business card front">
  <div class="gold-band">Residential/Commerical</div>

  <svg class="gold-arc" viewBox="0 0 857 500" aria-hidden="true">
    <defs>
      <linearGradient id="arcGold" x1="0" y1="0" x2="1" y2="0.35">
        <stop offset="0" stop-color="#f3cc72"/>
        <stop offset="0.3" stop-color="#d8ae5d"/>
        <stop offset="0.5" stop-color="#9a7430"/>
        <stop offset="0.72" stop-color="#d4ab5b"/>
        <stop offset="1" stop-color="#f0c96f"/>
      </linearGradient>
    </defs>
    <path d="M0 0 L50 0 A503 503 0 0 1 503 500 L0 500 Z" fill="url(#arcGold)"/>
  </svg>

  <div class="brand">
    <span class="brand__dot"></span>
    <span class="brand__name">HarlowForge</span>
  </div>

  <div class="contact-block">
    <h1 class="contact-block__name">Dale Morrow</h1>
    <p class="contact-block__title">President</p>
    <ul class="contact-list">
      <li>
        <svg viewBox="0 0 24 24" aria-hidden="true"><path d="M6.6 10.8a15.1 15.1 0 0 0 6.6 6.6l2.2-2.2a1 1 0 0 1 1-.25 11.4 11.4 0 0 0 3.6.57 1 1 0 0 1 1 1V20a1 1 0 0 1-1 1A17 17 0 0 1 3 4a1 1 0 0 1 1-1h3.5a1 1 0 0 1 1 1c0 1.25.2 2.46.57 3.6a1 1 0 0 1-.25 1z"/></svg>
        <span>405.618.7734</span>
      </li>
      <li>
        <svg viewBox="0 0 24 24" aria-hidden="true"><path d="M2 5h20v14H2z M3.5 6.5 12 12.5l8.5-6" fill="var(--ink)"/><path d="M3.5 7 12 13l8.5-6" fill="none" stroke="#e8c06a" stroke-width="1.6"/></svg>
        <span>dale@harlowforge.com</span>
      </li>
      <li>
        <svg viewBox="0 0 24 24" aria-hidden="true"><path d="M12 2a10 10 0 1 0 0 20 10 10 0 0 0 0-20zm6.9 6h-2.9a15.6 15.6 0 0 0-1.4-3.6A8 8 0 0 1 18.9 8zM12 4c.8 1.2 1.5 2.5 1.9 4h-3.8c.4-1.4 1.1-2.8 1.9-4zM4.3 14a8 8 0 0 1 0-4h3.4a16 16 0 0 0 0 4zm.8 2h2.9c.3 1.3.8 2.5 1.4 3.6A8 8 0 0 1 5.1 16zM8 8H5.1a8 8 0 0 1 4.3-3.6C8.8 5.5 8.4 6.7 8 8zm4 12c-.8-1.2-1.5-2.5-1.9-4h3.8c-.4 1.4-1.1 2.8-1.9 4zm2.3-6H9.7a14.6 14.6 0 0 1 0-4h4.6a14.6 14.6 0 0 1 0 4zm.3 5.6c.6-1.1 1.1-2.3 1.4-3.6h2.9a8 8 0 0 1-4.3 3.6zm1.7-5.6a16 16 0 0 0 0-4h3.4a8 8 0 0 1 0 4z"/></svg>
        <span>www.harlowforge.com</span>
      </li>
    </ul>
  </div>

  <p class="license">Lic #: 3917258</p>
</section>

<section class="card card--back" aria-label="Business card back">
  <div class="brand">
    <span class="brand__dot"></span>
    <span class="brand__name">HarlowForge</span>
  </div>
  <div class="gold-band">Residential/Commerical</div>
</section>

</body>
</html>
```